OVRA SaaS Dashboard design

We are looking to get three dashboard mockups designed in the look and feel of our SaaS application. We want the three mockup / wireframes's designed and delivered in .svg so that we can make text and logo changes for specific customer cases. The purpose of the design is to illustrate the capability of our SaaS platform in initial sales meeting and customized for specific customer use cases without having to create in our application.

Target Market(s)

Large enterprises, IT function & executive management

Number of Pages Required

3 page

Requirements
Must have
• Follow design guideline

```html
<!DOCTYPE html>
<html lang="en">
<head>
<meta charset="utf-8">
<title>LinkFlow Education Overview · OVRA Dashboard</title>
<link href="https://fonts.googleapis.com/css2?family=Montserrat:ital,wght@0,400;0,600;0,700;0,800;1,700;1,800&family=Source+Sans+3:wght@400;600&display=swap" rel="stylesheet">
<style>
  :root {
    --header-bg: #cccccc;
    --body-bg: #e4e4e4;
    --footer-bg: #cccccc;
    --panel-bg: #ffffff;
    --nav-active: #f2b42a;
    --nav-red: #ff3a5c;
    --nav-divider: #e8334f;
    --title-grey: #5e5e5e;
    --heading-grey: #a3a3a3;
    --blue: #0a66ff;
    --navy: #223459;
    --teal: #2fd4d6;
    --teal-light: #cde8ee;
    --track: #eaf3f6;
    --grid: #dbe9f0;
    --axis: #a9cfdf;
    --label: #3a7fa8;
    --alerts-bg: #454545;
    --alerts-line: #6a6a6a;
    --footer-text: #b3b3b3;
  }
  * { box-sizing: border-box; margin: 0; padding: 0; }
  html, body { width: 1200px; height: 675px; overflow: hidden; }
  body {
    position: relative;
    background: var(--body-bg);
    font-family: "Montserrat", sans-serif;
  }
  .app-header {
    position: absolute; left: 0; top: 0; width: 1200px; height: 71px;
    background: var(--header-bg);
  }
  .client-mark {
    position: absolute; left: 38px; top: 13px; width: 44px; text-align: center;
  }
  .client-mark .dot {
    width: 30px; height: 30px; border-radius: 50%;
    border: 2px solid #555; margin: 0 auto 4px;
  }
  .client-mark .name {
    font-size: 6px; font-weight: 800; color: #444; white-space: nowrap;
  }
  .app-title {
    position: absolute; left: 119px; top: 25px;
    font-size: 19.5px; font-weight: 700; color: var(--title-grey);
    letter-spacing: -0.1px;
  }
  .main-nav {
    position: absolute; left: 515px; top: 0; width: 599px; height: 71px;
    background: var(--nav-red); display: flex;
  }
  .main-nav a {
    display: flex; align-items: center; justify-content: center;
    height: 71px; color: #fff; text-decoration: none;
    font-size: 11.5px; font-weight: 600; position: relative;
  }
  .main-nav a + a::before {
    content: ""; position: absolute; left: 0; top: 8px; bottom: 5px;
    width: 1px; background: var(--nav-divider);
  }
  .main-nav a.is-active { background: var(--nav-active); }
  .main-nav a.is-active + a::before { display: none; }
  .account-brand {
    position: absolute; left: 1128px; top: 26px;
    font-size: 15px; font-weight: 800; color: #444; letter-spacing: 0.5px;
  }
  .panel {
    position: absolute; background: var(--panel-bg); border-radius: 3px;
  }
  .panel svg { display: block; width: 100%; height: 100%; }
  .panel-activity-1 { left: 40.5px; top: 82px; width: 443px; height: 252.5px; }
  .panel-activity-2 { left: 489px; top: 83.4px; width: 443px; height: 252.5px; }
  .panel-activity-3 { left: 40.5px; top: 341.5px; width: 443px; height: 252.5px; }
  .panel-activity-4 { left: 489px; top: 343px; width: 443px; height: 252.5px; }
  .panel-title { font-family: "Montserrat", sans-serif; font-style: italic; font-weight: 800; fill: var(--heading-grey); font-size: 40px; }
  .axis-label { font-family: "Source Sans 3", sans-serif; fill: var(--label); font-size: 22px; }
  .axis-label.small { font-size: 19px; }
  .grid { stroke: var(--grid); stroke-width: 2; }
  .axis { stroke: var(--axis); stroke-width: 3; fill: none; }
  .bar-blue { fill: var(--blue); }
  .bar-navy { fill: var(--navy); }
  .bar-teal { fill: var(--teal); }
  .bar-track { fill: var(--track); }
  .line-blue { stroke: var(--blue); stroke-width: 3.5; fill: none; }
  .line-teal { stroke: var(--teal); stroke-width: 3.5; fill: none; }
  .dot-blue { fill: var(--blue); }
  .dot-teal { fill: var(--teal); }
  .alerts {
    position: absolute; left: 938px; top: 83px; width: 205px; height: 513px;
    background: var(--alerts-bg); border-radius: 3px; padding: 0 9px 0 11px;
  }
  .alerts h2 {
    font-size: 11.5px; font-weight: 600; color: var(--nav-active);
    margin-top: 9px; height: 18px;
  }
  .alert-item {
    border-top: 1px solid var(--alerts-line); height: 69.8px; padding-top: 3px; color: #fff;
  }
  .alert-item:last-child { border-bottom: 1px solid var(--alerts-line); }
  .alert-item h3 { font-size: 6.4px; font-weight: 700; margin-bottom: 8px; }
  .alert-item p { font-size: 6.1px; line-height: 7.5px; text-align: justify; }
  .app-footer {
    position: absolute; left: 0; top: 608px; width: 1200px; height: 67px;
    background: var(--footer-bg);
  }
  .powered-by {
    position: absolute; left: 494px; top: 22px;
    font-size: 17px; font-weight: 800; font-style: italic; color: var(--footer-text);
  }
  .footer-brand {
    position: absolute; left: 611px; top: 17px; display: flex; align-items: center; gap: 8px;
    color: var(--footer-text); font-size: 26px; font-weight: 700; letter-spacing: 1px;
  }
  .footer-brand .dot {
    width: 20px; height: 20px; border-radius: 50%; border: 3px solid var(--footer-text);
  }
</style>
</head>
<body>
  <header class="app-header">
    <div class="client-mark"><div class="dot"></div><div class="name">CLIENT'S LOGO</div></div>
    <h1 class="app-title">LinkFlow Education Overview</h1>
    <nav class="main-nav">
      <a class="is-active" href="#" style="width:85px">Dashboard</a>
      <a href="#" style="width:94px">Environments</a>
      <a href="#" style="width:65px">Events</a>
      <a href="#" style="width:89px">Analytics</a>
      <a href="#" style="width:76px">Reports</a>
      <a href="#" style="width:90px">Performance</a>
      <a href="#" style="width:100px">Settings</a>
    </nav>
    <div class="account-brand">OVRA</div>
  </header>

  <section class="panel panel-activity-1">
    <svg viewBox="87 176 951 542" aria-label="Activity 1">
      <text class="panel-title" x="135" y="246">Activity 1</text>
      <circle cx="300" cy="508" r="123" fill="none" stroke="var(--teal-light)" stroke-width="26"/>
      <path d="M300 385 A123 123 0 0 1 300 631" fill="none" stroke="var(--teal)" stroke-width="26"/>
      <text x="306" y="535" text-anchor="middle" font-family="Source Sans 3, sans-serif" font-size="70" fill="var(--label)">50%</text>
      <g>
        <line class="grid" x1="617" y1="313" x2="967" y2="313"/>
        <line class="grid" x1="617" y1="379" x2="967" y2="379"/>
        <line class="grid" x1="617" y1="444" x2="967" y2="444"/>
        <line class="grid" x1="617" y1="510" x2="967" y2="510"/>
        <line class="grid" x1="617" y1="576" x2="967" y2="576"/>
      </g>
      <g class="axis-label" text-anchor="end">
        <text x="605" y="248">1100</text><text x="605" y="315">900</text><text x="605" y="382">700</text>
        <text x="605" y="450">500</text><text x="605" y="517">300</text><text x="605" y="584">100</text><text x="605" y="652">0</text>
      </g>
      <rect class="bar-blue" x="637" y="308" width="35" height="340"/>
      <rect class="bar-navy" x="671" y="470" width="35" height="178"/>
      <rect class="bar-blue" x="748" y="405" width="35" height="243"/>
      <rect class="bar-navy" x="783" y="243" width="35" height="405"/>
      <rect class="bar-blue" x="859" y="535" width="35" height="113"/>
      <rect class="bar-navy" x="894" y="340" width="35" height="308"/>
      <path class="axis" d="M617 235 V648 H967"/>
      <g class="axis-label" text-anchor="middle">
        <text x="668" y="691">2016</text><text x="786" y="691">2017</text><text x="905" y="691">2018</text>
      </g>
    </svg>
  </section>

  <section class="panel panel-activity-2">
    <svg viewBox="1050 179 951 542" aria-label="Activity 2">
      <text class="panel-title" x="1090" y="246">Activity 2</text>
      <g>
        <line class="grid" x1="1167" y1="291" x2="1943" y2="291"/>
        <line class="grid" x1="1167" y1="358" x2="1943" y2="358"/>
        <line class="grid" x1="1167" y1="428" x2="1943" y2="428"/>
        <line class="grid" x1="1167" y1="497" x2="1943" y2="497"/>
        <line class="grid" x1="1167" y1="567" x2="1943" y2="567"/>
      </g>
      <g class="axis-label" text-anchor="end">
        <text x="1155" y="295">1000</text><text x="1155" y="365">700</text><text x="1155" y="435">500</text>
        <text x="1155" y="505">300</text><text x="1155" y="575">100</text><text x="1155" y="645">0</text>
      </g>
      <g class="bar-blue">
        <rect x="1189" y="285" width="36" height="355"/>
        <rect x="1260" y="455" width="36" height="185"/>
        <rect x="1330" y="387" width="36" height="253"/>
        <rect x="1400" y="319" width="36" height="321"/>
        <rect x="1470" y="387" width="36" height="253"/>
        <rect x="1541" y="489" width="36" height="151"/>
        <rect x="1611" y="319" width="36" height="321"/>
        <rect x="1681" y="557" width="36" height="83"/>
        <rect x="1752" y="319" width="36" height="321"/>
        <rect x="1822" y="557" width="36" height="83"/>
        <rect x="1892" y="353" width="36" height="287"/>
      </g>
      <path class="axis" d="M1167 275 V640 H1943"/>
      <g class="axis-label" text-anchor="middle">
        <text x="1207" y="686">100</text><text x="1280" y="686">200</text><text x="1351" y="686">300</text>
        <text x="1422" y="686">400</text><text x="1493" y="686">500</text><text x="1564" y="686">600</text>
        <text x="1635" y="686">600</text><text x="1706" y="686">700</text><text x="1777" y="686">800</text>
        <text x="1848" y="686">900</text><text x="1918" y="686">1000</text>
      </g>
    </svg>
  </section>

  <section class="panel panel-activity-3">
    <svg viewBox="87 733 951 542" aria-label="Activity 3">
      <text class="panel-title" x="130" y="801">Activity 3</text>
      <g>
        <line class="grid" x1="225" y1="830" x2="846" y2="830"/>
        <line class="grid" x1="225" y1="886" x2="846" y2="886"/>
        <line class="grid" x1="225" y1="942" x2="846" y2="942"/>
        <line class="grid" x1="225" y1="997" x2="846" y2="997"/>
        <line class="grid" x1="225" y1="1053" x2="846" y2="1053"/>
      </g>
      <g class="axis-label small" text-anchor="end">
        <text x="214" y="832">1000</text><text x="214" y="888">700</text><text x="214" y="944">500</text>
        <text x="214" y="1000">300</text><text x="214" y="1056">100</text><text x="214" y="1112">0</text>
      </g>
      <path class="axis" d="M225 818 V1108 H846"/>
      <polyline class="line-teal" points="251,992 304,992 367,883 424,1102 483,940 548,940 592,1044 650,1044 709,991 760,1048 846,992"/>
      <g class="dot-teal">
        <circle cx="251" cy="992" r="6"/><circle cx="304" cy="992" r="6"/><circle cx="367" cy="883" r="6"/>
        <circle cx="424" cy="1102" r="6"/><circle cx="483" cy="940" r="6"/><circle cx="548" cy="940" r="6"/>
        <circle cx="592" cy="1044" r="6"/><circle cx="650" cy="1044" r="6"/><circle cx="709" cy="991" r="6"/>
        <circle cx="760" cy="1048" r="6"/>
      </g>
      <polyline class="line-blue" points="257,1044 306,1079 367,992 423,1046 483,992 591,992 650,877 708,1048 760,1048 846,830"/>
      <g class="dot-blue">
        <circle cx="257" cy="1044" r="6"/><circle cx="306" cy="1079" r="6"/><circle cx="367" cy="992" r="6"/>
        <circle cx="423" cy="1046" r="6"/><circle cx="483" cy="992" r="6"/><circle cx="591" cy="992" r="6"/>
        <circle cx="650" cy="877" r="6"/><circle cx="708" cy="1048" r="6"/><circle cx="846" cy="830" r="6"/>
      </g>
      <g class="axis-label small" text-anchor="middle">
        <text x="257" y="1145">100</text><text x="315" y="1145">200</text><text x="372" y="1145">300</text>
        <text x="429" y="1145">400</text><text x="486" y="1145">500</text><text x="542" y="1145">600</text>
        <text x="599" y="1145">600</text><text x="656" y="1145">700</text><text x="712" y="1145">800</text>
        <text x="769" y="1145">900</text><text x="826" y="1145">1000</text>
      </g>
      <rect class="bar-blue" x="221" y="1178" width="12" height="60"/>
      <text class="axis-label small" x="248" y="1203">Lorem ipsum dolor sit amet,</text>
      <text class="axis-label small" x="248" y="1226">consectetuer adipiscing eli.</text>
      <rect class="bar-teal" x="560" y="1178" width="12" height="60"/>
      <text class="axis-label small" x="587" y="1203">Lorem ipsum dolor sit amet,</text>
      <text class="axis-label small" x="587" y="1226">consectetuer adipiscing eli.</text>
    </svg>
  </section>

  <section class="panel panel-activity-4">
    <svg viewBox="1050 736 951 542" aria-label="Activity 4">
      <text class="panel-title" x="1106" y="804">Activity 4</text>
      <g class="bar-track">
        <rect x="1269" y="837" width="536" height="28"/><rect x="1269" y="882" width="536" height="28"/>
        <rect x="1269" y="928" width="536" height="28"/><rect x="1269" y="973" width="536" height="28"/>
        <rect x="1269" y="1019" width="536" height="28"/><rect x="1269" y="1065" width="536" height="28"/>
      </g>
      <g class="bar-teal">
        <rect x="1269" y="837" width="536" height="28"/><rect x="1269" y="882" width="193" height="28"/>
        <rect x="1269" y="928" width="381" height="28"/><rect x="1269" y="973" width="89" height="28"/>
        <rect x="1269" y="1019" width="469" height="28"/><rect x="1269" y="1065" width="307" height="28"/>
      </g>
      <g class="axis-label small" text-anchor="end">
        <text x="1257" y="857">Name 1</text><text x="1257" y="902">Name 2</text><text x="1257" y="948">Name 3</text>
        <text x="1257" y="993">Name 4</text><text x="1257" y="1039">Name 5</text><text x="1257" y="1087">Name 6</text>
      </g>
      <g class="axis-label" font-size="17" style="font-size:17px">
        <text x="1472" y="902">40%</text><text x="1659" y="948">70%</text><text x="1368" y="993">20%</text>
        <text x="1746" y="1040">80%</text><text x="1584" y="1085">60%</text>
        <text x="1270" y="1141">0%</text><text x="1858" y="1141" text-anchor="end">100%</text>
      </g>
      <path class="axis" d="M1267 826 V1107 H1860"/>
      <rect class="bar-teal" x="1273" y="1172" width="12" height="58"/>
      <text class="axis-label small" x="1298" y="1197">Lorem ipsum dolor sit amet,</text>
      <text class="axis-label small" x="1298" y="1219">consectetuer adipiscing eli.</text>
    </svg>
  </section>

  <aside class="alerts">
    <h2>Alerts</h2>
    <div class="alert-item"><h3>Activity 1: 01/05/2019</h3><p>Lorem ipsum dolor sit amet, consectetur adipiscing elit, sed do eiusmod tempor incididunt ut labore et dolore magna aliqua. Ut enim ad minim veniam, quis nostrud exercitation ullamco laboris nisi ut aliquip ex ea commodo consequat. Duis aute irure dolor in reprehenderit in voluptate velit esse cillum dolore eu fugiat nulla pariatur</p></div>
    <div class="alert-item"><h3>Activity 2: 02/05/2019</h3><p>Lorem ipsum dolor sit amet, consectetur adipiscing elit, sed do eiusmod tempor incididunt ut labore et dolore magna aliqua. Ut enim ad minim veniam, quis nostrud exercitation ullamco laboris nisi ut aliquip ex ea commodo consequat. Duis aute irure dolor in reprehenderit in voluptate velit esse cillum dolore eu fugiat nulla pariatur</p></div>
    <div class="alert-item"><h3>Activity 3: 03/05/2019</h3><p>Lorem ipsum dolor sit amet, consectetur adipiscing elit, sed do eiusmod tempor incididunt ut labore et dolore magna aliqua. Ut enim ad minim veniam, quis nostrud exercitation ullamco laboris nisi ut aliquip ex ea commodo consequat. Duis aute irure dolor in reprehenderit in voluptate velit esse cillum dolore eu fugiat nulla pariatur</p></div>
    <div class="alert-item"><h3>Activity 4: 04/05/2019</h3><p>Lorem ipsum dolor sit amet, consectetur adipiscing elit, sed do eiusmod tempor incididunt ut labore et dolore magna aliqua. Ut enim ad minim veniam, quis nostrud exercitation ullamco laboris nisi ut aliquip ex ea commodo consequat. Duis aute irure dolor in reprehenderit in voluptate velit esse cillum dolore eu fugiat nulla pariatur</p></div>
    <div class="alert-item"><h3>Activity 5: 05/05/2019</h3><p>Lorem ipsum dolor sit amet, consectetur adipiscing elit, sed do eiusmod tempor incididunt ut labore et dolore magna aliqua. Ut enim ad minim veniam, quis nostrud exercitation ullamco laboris nisi ut aliquip ex ea commodo consequat. Duis aute irure dolor in reprehenderit in voluptate velit esse cillum dolore eu fugiat nulla pariatur</p></div>
    <div class="alert-item"><h3>Activity 6: 06/05/2019</h3><p>Lorem ipsum dolor sit amet, consectetur adipiscing elit, sed do eiusmod tempor incididunt ut labore et dolore magna aliqua. Ut enim ad minim veniam, quis nostrud exercitation ullamco laboris nisi ut aliquip ex ea commodo consequat. Duis aute irure dolor in reprehenderit in voluptate velit esse cillum dolore eu fugiat nulla pariatur</p></div>
  </aside>

  <footer class="app-footer">
    <span class="powered-by">Powered by</span>
    <span class="footer-brand"><span class="dot"></span>OVRA</span>
  </footer>
</body>
</html>
```